12 Week Brisk Peak Lean Form Challenge Flyer

Hi,
We are a tennis coaching business called Vantle Racquet based in Sydney Australia. We are looking to launch a new 12 week fitness program called "12 Week Brisk Peak Form Lean Challenge"
We would like the flyer to utilise the colours green and yellow reflecting the tennis theme - however we don't necessarily want it to look like a tennis flyer as tennis is only a small piece of the program via our tennis cardio workouts. We are using tennis cardio as a fitness thing.
We are based in Australia where spring is about to start and everyone is looking to get fit and beach ready for summer so we would like the flyer to communicate fitness, energy, vitality etc. = a Brisk Peak Life !
SPECIFICALLY ON THE FLYER WE WOULD LIKE THE FOLLOWING INFO:
Get a Brisk Peak Form. Live a Brisk Peak Life. In Just 12 Weeks.
Take the challenge today !
Your challenge should you choose to accept it will include:
3 weekly 1hr group training sessions using fast, high intensity & seriously fun cardio workouts. with music to pump you up.
90 Day weight management & nutrition plan using revolutionary nutritional, all natural products. (All products included)
12 Week E-Course covering the dieting dilemma, exercise, stress management and sleep.
Personalised & interactive online membership program which includes:
- Customised meal plans based on your personal nutrition parameters & food preferences
- Step by Step guide to achieving your health goals
- Interactive goal setting charts to track your progress
- Delicious recipe database & thousands of meal options
- Easy interactive nutrition and exercise journal
- Full nutrition support from our team of experts
It's time to take action & get Brisk Peak Form Lean !
Only $99 per week !!
Join TODAY
Starts September 17th.
Call 02 7381 2459 or email us at info@vantleracquet.example
Please let us know if you need any more info.
Our website is www.vantleracquet.example if you want to see more about us but again please keep in mind this is not being marketed as a tennis specific program ... more of a fitness, get ready for summer program.
Thanks
Gwendolyn
Target Market(s)
Men and women between ages of 27-45 years
Industry/Entity Type
Nutrition

```html
<!DOCTYPE html>
<html lang="en">
<head>
<meta charset="utf-8">
<title>12 Week Brisk Peak Lean Form Challenge</title>
<link rel="stylesheet" href="https://fonts.googleapis.com/css2?family=Dosis:wght@400;500&family=Exo+2:wght@700;800&display=swap">
<style>
  :root {
    --green: #5e8b35;
    --green-light: #8dc63f;
    --yellow: #f6e21c;
    --olive: #b19b2b;
    --ink: #1d1d1b;
    --body-ink: #3a3a3a;
    --paper: #ffffff;
    --photo-light: #eef1f2;
    --photo-mid: #d9c3ae;
    --photo-dark: #8f8a86;
  }
  * { margin: 0; padding: 0; box-sizing: border-box; }
  html, body { width: 849px; height: 1200px; overflow: hidden; background: var(--paper); }
  .flyer { position: relative; width: 849px; height: 1200px; overflow: hidden; background: var(--paper); }
  .artwork { position: absolute; inset: 0; width: 849px; height: 1200px; }
  .headline {
    position: absolute; right: 50px; top: 524px; text-align: right;
    font-family: "Exo 2", sans-serif; font-weight: 800; font-size: 20.5px; line-height: 27px;
  }
  .headline .green { color: var(--green); display: block; }
  .headline .olive { color: var(--olive); display: block; }
  .details {
    position: absolute; right: 50px; top: 648px; width: 560px; text-align: right;
    font-family: "Dosis", sans-serif; font-weight: 400; font-size: 15.5px; line-height: 20.5px;
    color: var(--body-ink); list-style: none;
  }
  .details p { margin-bottom: 20px; }
  .details .group { margin-bottom: 20px; }
  .action {
    position: absolute; left: 0; width: 849px; top: 1012px; text-align: center;
    font-family: "Exo 2", sans-serif; font-weight: 700; font-size: 18.5px; color: var(--green);
  }
  .offer {
    position: absolute; left: 140px; top: 1068px;
    font-family: "Exo 2", sans-serif; font-weight: 700; font-size: 15.5px; color: var(--ink);
  }
  .contact {
    position: absolute; left: 252px; top: 1118px;
    font-family: "Exo 2", sans-serif; font-weight: 700; font-size: 15px; color: var(--paper); line-height: 22px;
  }
  .contact .label { font-weight: 700; }
  .contact .phone { font-size: 21px; font-weight: 800; }
  .contact .email-line { display: block; padding-left: 52px; }
</style>
</head>
<body>
<main class="flyer">
  <svg class="artwork" viewBox="0 0 849 1200" xmlns="http://www.w3.org/2000/svg">
    <defs>
      <linearGradient id="photoTone" x1="0" y1="0" x2="1" y2="0.4">
        <stop offset="0" stop-color="var(--photo-mid)"/>
        <stop offset="0.45" stop-color="var(--photo-light)"/>
        <stop offset="1" stop-color="var(--photo-dark)"/>
      </linearGradient>
    </defs>
    <polygon role="img" aria-label="Photo of smiling people riding exercise bikes in a bright gym class"
             points="0,0 849,0 849,504 470,504 250,720 0,720" fill="url(#photoTone)"/>
    <g class="light-bands" fill="#ffffff" opacity="0.45">
      <polygon points="160,640 230,640 720,150 650,150"/>
      <polygon points="250,560 300,560 780,80 730,80"/>
      <polygon points="330,480 360,480 849,0 819,0"/>
      <polygon points="80,620 110,620 620,110 590,110"/>
    </g>
    <g class="accent-stripes-top">
      <polygon points="600,10 630,10 560,80 530,80" fill="var(--green)"/>
      <polygon points="690,30 700,30 610,120 600,120" fill="var(--green)"/>
      <polygon points="760,40 790,40 770,62 740,62" fill="var(--yellow)"/>
      <polygon points="740,70 770,70 730,112 700,112" fill="var(--green-light)"/>
      <polygon points="820,220 849,220 849,236 806,236" fill="var(--green)"/>
      <rect x="730" y="238" width="45" height="3" fill="var(--olive)"/>
    </g>
    <g class="accent-stripes-bottom">
      <polygon points="0,600 110,600 90,625 0,625" fill="var(--yellow)"/>
      <polygon points="70,645 165,645 110,705 30,705" fill="var(--green-light)"/>
      <polygon points="0,620 30,620 0,650" fill="var(--green)"/>
      <polygon points="130,700 250,700 130,820 10,820 10,815 120,705" fill="var(--yellow)"/>
      <polygon points="0,700 130,700 22,847 0,847" fill="var(--yellow)"/>
      <polygon points="0,820 60,760 64,764 0,828" fill="var(--green)"/>
      <polygon points="250,700 256,700 150,806 144,806" fill="var(--olive)"/>
    </g>
    <polygon class="offer-band" points="140,1053 797,1053 770,1106 103,1106" fill="var(--yellow)"/>
    <polygon class="contact-band" points="200,1108 705,1108 645,1172 145,1172" fill="var(--green)"/>
  </svg>

  <h1 class="headline">
    <span class="green">Get a Brisk Peak Form.</span>
    <span class="green">Live a Brisk Peak Life.</span>
    <span class="olive">In Just 12 Weeks.</span>
    <span class="olive">Take the challenge today!</span>
  </h1>

  <section class="details">
    <p>Our challenge should you choose to accept it will include:</p>
    <div class="group">
      3 weekly 1hr group training sessions using fast, high intensity &amp; seriously<br>
      fun cardio workouts with music to pump you up.<br>
      90 Day weight management &amp; nutrition plan using revolutionary<br>
      nutritional, all natural products. (All products included)<br>
      12 Week E-Course covering the dieting dilemma, exercise,<br>
      stress management and sleep.
    </div>
    <div class="group">
      Personalised &amp; interactive online membership program which includes:<br>
      - Customised meal plans based on your personal nutrition<br>
      parameters &amp; food preferences<br>
      - Step by Step guide to achieving your health goals<br>
      - Interactive goal setting charts to track your progress<br>
      - Delicious recipe database &amp; thousands of meal options<br>
      - Easy interactive nutrition and exercise journal<br>
      - Full nutrition support from our team of experts
    </div>
  </section>

  <p class="action">It's time to take action &amp; get Brisk Peak Form Lean !</p>

  <p class="offer">Only $99 per week !! • Join TODAY • Starts September 17th.</p>

  <p class="contact">
    <span class="label">Call</span> <span class="phone">02 7381 2459</span>
    <span class="email-line">or email us at info@vantleracquet.example</span>
  </p>
</main>
</body>
</html>
```